Private Learning Centre in Singapore needs a flyer design

We need a flyer design for our upcoming education fair and also able to use it for day to day purpose. The aim is to attract parents, students to enrol for classes by offering them free trial class/assessment. 2 sided flyer with the front page as the logo only and details on the other page. We would like to see a final design in blue, white and it should be curious and attractive enough not to allow customers to throw it away once they received it.

Education

```html
<!DOCTYPE html>
<html lang="en">
<head>
<meta charset="utf-8">
<title>Bright Path Academy – Flyer</title>
<link rel="stylesheet" href="https://fonts.googleapis.com/css2?family=Source+Sans+3:ital,wght@0,700;1,700&display=swap">
<style>
  :root {
    --brand-blue: #3c55a5;
    --deep-blue: #2f4a9e;
    --sky-blue: #1d9ad6;
    --pale-blue: #cfe6f6;
    --white: #ffffff;
    --page: #eef1f5;
  }
  * { box-sizing: border-box; margin: 0; padding: 0; }
  html, body {
    width: 877px; height: 1200px; overflow: hidden;
    background: var(--page);
    font-family: "Source Sans 3", "Myriad Pro", sans-serif;
  }
  .flyer { position: relative; width: 877px; height: 1200px; }

  /* Front side */
  .front-side {
    position: absolute; left: 60px; top: 69px; width: 706px; height: 491px;
    background: var(--brand-blue);
  }
  .front-emblem {
    position: absolute; left: 178px; top: 65px; width: 350px; height: 350px;
    border-radius: 50%; background: var(--white);
    display: flex; align-items: center; justify-content: center; text-align: center;
  }
  .front-emblem .brand-name {
    color: var(--brand-blue); font-weight: 700; font-size: 38px;
    line-height: 1.15; letter-spacing: 2px; text-transform: uppercase;
  }

  /* Back side */
  .back-side {
    position: absolute; left: 119px; top: 643px; width: 705px; height: 489px;
    overflow: hidden;
    background: radial-gradient(ellipse 75% 70% at 50% 40%, var(--white) 35%, var(--pale-blue) 100%);
  }
  .offer { position: absolute; left: 45px; top: 72px; color: var(--deep-blue); font-weight: 700; }
  .offer-main { display: block; font-size: 52px; line-height: 44px; letter-spacing: 1px; }
  .offer-sub { display: block; font-size: 21px; line-height: 24px; margin-top: 2px; }
  .students-photo {
    position: absolute; left: 217px; top: 51px; width: 464px; height: 111px;
    background: linear-gradient(90deg, #e85a3a, #9ccb4a 25%, #e05c98 45%, #d8383f 62%, #f3c23b 80%, #3aa7dd);
    opacity: 0.85; border-radius: 4px;
  }
  .tick-badge { position: absolute; left: 33px; top: 192px; width: 70px; height: 70px; }
  .intro {
    position: absolute; left: 111px; top: 186px; width: 580px;
    color: var(--deep-blue); font-style: italic; font-weight: 700;
    font-size: 18.5px; line-height: 25px;
  }
  .wave { position: absolute; left: 0; top: 300px; width: 705px; height: 110px; }
  .back-emblem {
    position: absolute; left: 1px; top: 317px; width: 134px; height: 134px;
    border-radius: 50%; background: var(--white); border: 3px solid var(--brand-blue);
    display: flex; align-items: center; justify-content: center; text-align: center;
  }
  .back-emblem .brand-name {
    color: var(--brand-blue); font-weight: 700; font-size: 15px;
    line-height: 1.15; letter-spacing: 1px; text-transform: uppercase;
  }
  .social {
    position: absolute; left: 299px; top: 436px; height: 31px;
    display: flex; align-items: center; gap: 6px;
    color: var(--deep-blue); font-weight: 700;
  }
  .social-square { width: 26px; height: 26px; background: var(--brand-blue); }
  .social-text { font-size: 11px; line-height: 12px; }
  .social-text strong { display: block; font-size: 17px; line-height: 17px; }
  .contact {
    position: absolute; right: 21px; top: 395px; text-align: right;
    color: var(--deep-blue); font-style: italic; font-weight: 700;
    font-size: 15px; line-height: 25.5px; list-style: none;
  }
</style>
</head>
<body>
<main class="flyer">
  <section class="front-side" aria-label="Flyer front">
    <div class="front-emblem">
      <span class="brand-name">Bright Path<br>Academy</span>
    </div>
  </section>

  <section class="back-side" aria-label="Flyer back">
    <div class="wave" aria-hidden="true">
      <svg width="705" height="110" viewBox="0 0 705 110">
        <path d="M0 62 C 200 100, 430 70, 705 8 L705 40 C 450 95, 220 120, 0 95 Z" fill="var(--sky-blue)"/>
        <path d="M0 50 C 210 85, 440 55, 705 0 L705 10 C 440 68, 210 98, 0 66 Z" fill="var(--pale-blue)"/>
        <path d="M0 95 C 220 120, 450 95, 705 40 L705 52 C 460 105, 230 128, 0 108 Z" fill="var(--deep-blue)" opacity="0.55"/>
      </svg>
    </div>

    <h2 class="offer"><span class="offer-main">FREE</span><span class="offer-sub">TRIAL CLASS</span></h2>

    <div class="students-photo" role="img" aria-label="Photo of a row of children lying down reading colourful books"></div>

    <svg class="tick-badge" viewBox="0 0 70 70" aria-hidden="true">
      <circle cx="35" cy="35" r="35" fill="var(--brand-blue)"/>
      <path d="M20 36 L31 47 L51 25" fill="none" stroke="var(--white)" stroke-width="6" stroke-linecap="round" stroke-linejoin="round"/>
    </svg>

    <p class="intro">Bright Path Academy is where you can develop academic and life skills. Our teachers are the heartbeat of the business. They inspire and nurture students, helping them surpass their expectations. We cover English, Mathematics and Science from Primary and Secondary Levels.</p>

    <div class="back-emblem">
      <span class="brand-name">Bright Path<br>Academy</span>
    </div>

    <div class="social">
      <span class="social-square" aria-hidden="true"></span>
      <span class="social-text">Find us on<strong>Chatterbook</strong></span>
    </div>

    <ul class="contact">
      <li>tel. 6100 2040 555</li>
      <li>Meridian Park Road S400123</li>
      <li>hello@brightpathacademy.com</li>
    </ul>
  </section>
</main>
</body>
</html>
```